Plakat-Design für Förderverein einer Feuerwehr
Zielgruppe
Wir sind ein Förderverein einer Feuerwehr und suchen ein modernes Design für unser Banner und Plakat für das Maifest
Aufgabenstellung
Das Banner soll die Maße von 2x1m haben und das Plakat soll das Format A3 haben. Der Textinhalt soll so bleiben.

```html
<!DOCTYPE html>
<html lang="de">
<head>
<meta charset="utf-8">
<title>Maifest – Plakat und Banner</title>
<link rel="stylesheet" href="https://fonts.googleapis.com/css2?family=Archivo+Black&family=Fira+Sans:wght@600;700;800&family=Fira+Sans+Condensed:wght@500&display=swap">
<style>
:root{
  --red:#e8001c;
  --red-deep:#d40018;
  --red-bright:#ff0a2a;
  --white:#ffffff;
  --cream:#ece6da;
  --ink:#141414;
  --stage:#e9e9e9;
}
*{margin:0;padding:0;box-sizing:border-box}
html,body{width:1037px;height:1200px;overflow:hidden;background:var(--stage)}
.canvas{position:relative;width:1037px;height:1200px}
.title{font-family:"Archivo Black",sans-serif;color:var(--white);line-height:1;white-space:nowrap;letter-spacing:1px}
.body-text{font-family:"Fira Sans",sans-serif;font-weight:700;color:var(--white);text-align:center;line-height:1.2}

/* Plakat */
.poster{position:absolute;left:359px;top:83px;width:318px;height:472px;background:radial-gradient(ellipse at 50% 45%,var(--red) 0%,var(--red-deep) 100%);overflow:hidden;box-shadow:0 4px 14px rgba(0,0,0,.25)}
.poster .title{position:absolute;left:18px;top:22px;font-size:57px;color:var(--cream)}
.poster .venue{position:absolute;left:18px;top:74px;width:282px;font-size:11px;color:var(--cream);text-align:center;font-family:"Fira Sans",sans-serif;font-weight:800}
.poster .emblem{position:absolute;left:59px;top:117px;width:200px;height:200px}
.poster .program{position:absolute;left:60px;top:341px;width:200px}
.poster .program p{font-size:11px;margin-bottom:8px;color:var(--cream)}
.poster .date{position:absolute;left:241px;top:370px;width:70px;height:102px;background:var(--cream);text-align:center;padding-top:6px}
.poster .date .day{font-family:"Fira Sans",sans-serif;font-weight:600;font-size:11px;color:var(--ink)}
.poster .date .num{font-family:"Archivo Black",sans-serif;font-size:40px;line-height:.95;color:var(--red)}
.poster .date .month{font-family:"Archivo Black",sans-serif;font-size:23px;line-height:1;color:var(--red)}
.poster .date .time{margin:5px 5px 0;border-top:1px solid var(--ink);border-bottom:1px solid var(--ink);font-family:"Fira Sans",sans-serif;font-weight:800;font-size:7px;color:var(--ink);padding:1px 0}
.poster .footer{position:absolute;left:0;bottom:0;width:318px;height:21px;background:var(--ink)}
.poster .footer span{position:absolute;left:10px;top:6px;font-family:"Fira Sans",sans-serif;font-weight:700;font-size:6px;color:var(--white)}

/* Banner */
.banner{position:absolute;left:0;top:682px;width:1037px;height:518px;background:radial-gradient(ellipse at 70% 50%,var(--red-bright) 0%,var(--red) 70%);overflow:hidden}
.banner .emblem{position:absolute;left:70px;top:50px;width:400px;height:400px}
.banner .title{position:absolute;left:522px;top:46px;font-size:96px}
.banner .venue{position:absolute;left:524px;top:135px;width:478px;font-family:"Fira Sans",sans-serif;font-weight:800;font-size:20px;color:var(--white);text-align:center;white-space:nowrap}
.banner .program{position:absolute;left:580px;top:188px;width:366px}
.banner .program p{font-size:23px;margin-bottom:12px}
.banner .footer{position:absolute;left:0;bottom:0;width:1037px;height:40px;background:#1f1f1f}
.banner .footer span{position:absolute;left:46px;top:11px;font-family:"Fira Sans",sans-serif;font-weight:700;font-size:13px;color:var(--white)}
.banner .date{position:absolute;left:648px;top:386px;width:232px;height:132px;background:var(--white);text-align:center;padding-top:6px;z-index:2}
.banner .date .day{font-family:"Fira Sans Condensed",sans-serif;font-weight:500;font-size:33px;letter-spacing:6px;color:var(--ink);line-height:1}
.banner .date .full{font-family:"Archivo Black",sans-serif;font-size:49px;line-height:1;color:var(--red);letter-spacing:-1px}
.banner .date .time{margin:8px 10px 0;border-top:2px solid var(--ink);border-bottom:2px solid var(--ink);font-family:"Fira Sans",sans-serif;font-weight:800;font-size:13px;color:var(--ink);padding:2px 0}
</style>
</head>
<body>
<div class="canvas">

  <section class="poster">
    <h1 class="title">MAIFEST</h1>
    <p class="venue">Feuerwehrgerätehaus Wiesenbacher Straße</p>
    <svg class="emblem" viewBox="0 0 200 200" role="img" aria-label="Feuerwehr-Emblem: vier Feuerwehrleute beim Löschen, Retten, Bergen und Schützen in einem geteilten Kreis">
      <circle cx="100" cy="100" r="97" fill="var(--cream)"/>
      <circle cx="100" cy="100" r="91" fill="var(--red-deep)"/>
    </svg>
    <div class="program">
      <p class="body-text">Ausstellung der Fahrzeuge</p>
      <p class="body-text">Kinderunterhaltung mit<br>Hüpfburg und mehr</p>
      <p class="body-text">Softdrinks, Bier vom Fass,<br>Grill-Spezialitäten</p>
    </div>
    <div class="footer"><span>Förderverein der Freiwillige Feuerwehr Löschzug Wiesenbach e.V.</span></div>
    <div class="date">
      <div class="day">SAMSTAG</div>
      <div class="num">25</div>
      <div class="month">MAI</div>
      <div class="time">AB 12:00 UHR</div>
    </div>
  </section>

  <section class="banner">
    <svg class="emblem" viewBox="0 0 400 400" role="img" aria-label="Feuerwehr-Emblem: vier Feuerwehrleute beim Löschen, Retten, Bergen und Schützen in einem geteilten Kreis">
      <circle cx="200" cy="200" r="200" fill="var(--white)"/>
      <circle cx="200" cy="200" r="191" fill="var(--red-deep)"/>
    </svg>
    <h1 class="title">MAIFEST</h1>
    <p class="venue">Feuerwehrgerätehaus Wiesenbacher Straße</p>
    <div class="program">
      <p class="body-text">Ausstellung der Fahrzeuge</p>
      <p class="body-text">Kinderunterhaltung mit<br>Hüpfburg und mehr</p>
      <p class="body-text">Softdrinks, Bier vom Fass,<br>Grill-Spezialitäten</p>
    </div>
    <div class="footer"><span>Förderverein der Freiwillige Feuerwehr Löschzug Wiesenbach e.V.</span></div>
    <div class="date">
      <div class="day">SAMSTAG</div>
      <div class="full">25. MAI</div>
      <div class="time">AB 12:00 UHR</div>
    </div>
  </section>

</div>
</body>
</html>
```